IT Distribution Wholesale Business Card & Logo Design

I need both logo and a business card that suits our business model, am happy to pay more for great effort put in.
Brevon Orbital Australia Pty Ltd
An IT Distribution / Wholesale company that distributes technology hardwares, softwares, components, etc.
Offer drop ship services for online retailers and supply to Australia-wide.
Based in Sydney Australia.
Design should give impressions of trust and stability.

Slogan: "your one stop technology supplier"
*two-sided name card
*logo + slogan on the back of the card

I don't have much specific requirements, leave it to designers to come up with creative & interesting masterpiece.
The logo and business card comes in first which i would like it to be completed latest by mid of March, we will require a whole redesign of our web pages, banner design, catalogue design later part.

Goodluck & thank you for your effort.

Hello designers,

Busy week, very good return rate on the number of designs and effort put into our business card design.
I thank you all for that.
We will have to extend this project for another week to two to receive more designs and more time for me to post some updates to you all.
We are getting there, i really liked some of the designs sent but just not the perfect masterpiece we are looking for.

Cheers,
Darnell Q.

Target Market(s)

Computer Retailers, Corporate, Schools, Councils.

Industry/Entity Type

Business

Requirements
Must have
• Brevon Orbital (Australia) Pty Ltd, Darnell Quist, Managing Director, Unit C, 14-18 Pellham Road, Dunmore NSW 2461, Ph +61 2 5037 1942, M +61 4 70395216, E darnell@brevonorbital.com.au, W www.brevonorbital.com.au
Nice to have
• Keep it simple & comfortable.
Target audiences are mostly >30-40 years old range.

Example of companies in the same line:-
http://www.kzp.com.au
http://www.norvix.com.au/
http://www.supplyhaventrade.com/
http://www.quenby.com.au/
http://www.bq456.com.au/
https://www.swiftgridhub.com.au/
http://carvelo.com.au/

```html
<!DOCTYPE html>
<html lang="en">
<head>
<meta charset="utf-8">
<title>Brevon Orbital – Business Card</title>
<link rel="stylesheet" href="https://fonts.googleapis.com/css2?family=Righteous&family=Pinyon+Script&display=swap">
<style>
  :root {
    --page: #ffffff;
    --ink-white: #ffffff;
    --ink-grey: #8a8fa8;
    --ink-silver: #b9bdc8;
    --blue-bright: #1436ff;
    --blue-mid: #0a1fd0;
    --blue-deep: #06107a;
    --navy: #03062a;
    --black: #000000;
    --cyan: #19d6e6;
    --brand-blue: #2a4bff;
  }
  * { margin: 0; padding: 0; box-sizing: border-box; }
  html, body { width: 1200px; height: 1200px; overflow: hidden; background: var(--page); }
  .canvas { position: relative; width: 1200px; height: 1200px; font-family: "Righteous", sans-serif; }

  .card {
    position: absolute;
    left: 102px;
    width: 1008px;
    height: 588px;
    overflow: hidden;
  }

  /* Front side */
  .card--front {
    top: 0;
    background:
      radial-gradient(ellipse 260px 190px at 280px 290px, rgba(25,214,230,0.55), rgba(25,214,230,0) 100%),
      linear-gradient(180deg, var(--black) 0%, #040a3a 14%, var(--blue-mid) 34%, var(--blue-bright) 48%, var(--blue-mid) 62%, #040a3a 82%, var(--black) 100%);
  }
  .brand-mark {
    position: absolute;
    left: 92px;
    top: 272px;
    display: flex;
    align-items: center;
    gap: 12px;
  }
  .brand-mark__square {
    width: 26px; height: 26px;
    background: var(--brand-blue);
  }
  .brand-mark__name {
    font-family: "Righteous", sans-serif;
    font-size: 30px;
    color: var(--ink-white);
    line-height: 1;
  }
  .contact {
    position: absolute;
    left: 352px;
    top: 196px;
    color: var(--ink-white);
    font-size: 17px;
    line-height: 1;
    text-shadow: 2px 2px 3px rgba(0,0,0,0.7);
  }
  .contact__company { color: var(--ink-grey); margin-bottom: 13px; }
  .contact__line { margin-bottom: 9px; }
  .contact__line--gap { margin-top: 14px; }
  .signature {
    position: absolute;
    right: 24px;
    top: 538px;
    font-size: 17px;
    color: var(--ink-white);
    text-shadow: 2px 2px 3px rgba(0,0,0,0.7);
  }
  .signature__name { color: var(--ink-grey); }

  /* Back side */
  .card--back {
    top: 594px;
    background:
      radial-gradient(ellipse 300px 260px at 220px 300px, rgba(25,214,230,0.75), rgba(25,214,230,0.15) 60%, rgba(25,214,230,0) 100%),
      linear-gradient(180deg, var(--blue-bright) 0%, var(--blue-mid) 35%, var(--blue-deep) 65%, var(--navy) 100%);
  }
  .back-brand {
    position: absolute;
    left: 86px;
    top: 150px;
    display: flex;
    align-items: center;
    gap: 18px;
  }
  .back-brand__square {
    width: 44px; height: 44px;
    background: var(--navy);
  }
  .back-brand__name {
    font-family: "Righteous", sans-serif;
    font-size: 64px;
    line-height: 1;
    color: var(--navy);
  }
  .slogan {
    position: absolute;
    left: 86px;
    top: 432px;
    font-family: "Pinyon Script", cursive;
    font-size: 40px;
    color: var(--ink-silver);
    text-shadow: 2px 2px 3px rgba(0,0,0,0.6);
  }
</style>
</head>
<body>
<main class="canvas">
  <section class="card card--front" aria-label="Card front">
    <div class="brand-mark">
      <span class="brand-mark__square"></span>
      <span class="brand-mark__name">Brevon Orbital</span>
    </div>
    <div class="contact">
      <p class="contact__company">Brevon Orbital (Australia) Pty Ltd</p>
      <p class="contact__line">Unit C, 14-18 Pellham Road</p>
      <p class="contact__line">Dunmore NSW 2461</p>
      <p class="contact__line">Ph +61 2 5037 1942</p>
      <p class="contact__line contact__line--gap">M +61 4 70395216</p>
      <p class="contact__line contact__line--gap">E darnell@brevonorbital.com.au</p>
      <p class="contact__line">W www.brevonorbital.com.au</p>
    </div>
    <p class="signature"><span class="signature__name">Darnell Quist</span>, Managing Director</p>
  </section>

  <section class="card card--back" aria-label="Card back">
    <div class="back-brand">
      <span class="back-brand__square"></span>
      <span class="back-brand__name">Brevon Orbital</span>
    </div>
    <p class="slogan">your one stop technology supplier</p>
  </section>
</main>
</body>
</html>
```